UNIQUE, Elegant business card for transport company.

MUST BE AN ACTUAL GRAPHIC DESIGNER.
NO TEMPLATES, NO MOCKUP GENERATORS.
Looking for a top notch, head turning, business card.
Will be printed on premium luxury paper with spot glossing and debossing.
Must know how to set up for spot glossing. Must be willing to work on the file to meet printers spec after final design.

Target Market(s)

All info on .psd file

Contact Information for Business Card

All info on .psd file

Requirements
Must have
• All info on .psd file
Nice to have
• All info on .psd file
Should not have
• Nothing red

```html
<!DOCTYPE html>
<html lang="en">
<head>
<meta charset="utf-8">
<title>Kestrel Freight business card</title>
<link href="https://fonts.googleapis.com/css2?family=Poppins:ital,wght@0,300;0,400;0,600;1,400;1,500&display=swap" rel="stylesheet">
<style>
  :root {
    --backdrop: #8a8a8a;
    --card: #222122;
    --accent: #1a9bd0;
    --ink-soft: #9a9a9a;
    --ink-mid: #b4b4b4;
    --mark: #3c3c3e;
    --mark-text: #4a4a4c;
    --white: #ffffff;
  }
  * { box-sizing: border-box; margin: 0; padding: 0; }
  html, body { width: 963px; height: 1200px; overflow: hidden; }
  body {
    background: var(--backdrop);
    font-family: "Poppins", sans-serif;
    position: relative;
  }
  .card {
    position: absolute;
    left: 131px;
    width: 700px;
    height: 400px;
    background: var(--card);
    overflow: hidden;
  }
  .card--front { top: 160px; }
  .card--back { top: 640px; }

  .brand-mark {
    position: absolute;
    left: 50%;
    transform: translateX(-50%);
    border-radius: 50%;
    background: var(--mark);
  }
  .card--front .brand-mark { top: 62px; width: 96px; height: 96px; }
  .card--back .brand-mark { top: 82px; width: 150px; height: 150px; }

  .holder-name {
    position: absolute; top: 193px; width: 100%;
    text-align: center; color: var(--accent);
    font-weight: 600; font-size: 27px; letter-spacing: 0.2px;
  }
  .holder-role {
    position: absolute; top: 225px; width: 100%;
    text-align: center; color: var(--ink-soft);
    font-style: italic; font-size: 14px;
  }
  .contact {
    position: absolute; top: 256px; width: 100%;
    text-align: center; color: var(--ink-soft);
    font-weight: 300; font-size: 14px; line-height: 18.7px;
  }
  .tagline-band {
    position: absolute; top: 345px; width: 100%; height: 29px;
    background: var(--accent); color: var(--white);
    text-align: center; font-style: italic; font-weight: 500;
    font-size: 14px; line-height: 29px;
  }
  .company-name {
    position: absolute; top: 297px; width: 100%;
    text-align: center; color: var(--mark-text);
    font-weight: 600; font-size: 24px; letter-spacing: 1px;
  }
</style>
</head>
<body>
  <section class="card card--front">
    <div class="brand-mark" aria-hidden="true"></div>
    <h1 class="holder-name">MARCUS HALE</h1>
    <p class="holder-role">Transporter</p>
    <p class="contact">
      P. (800) RIDE KFT P. (555) 210-4471 C. (555) 382-9057<br>
      F. (555) 640-1128 E. marcus@kestrelfreight.com W. kestrelfreight.com<br>
      2400 Ridgeline Avenue, NE, Marietta, Georgia, 30060<br>
      US DOT 5281064 | MC # 7730412
    </p>
    <div class="tagline-band">Licensed. Bonded. Insured.</div>
  </section>

  <section class="card card--back">
    <div class="brand-mark" aria-hidden="true"></div>
    <p class="company-name">KESTREL FREIGHT, INC.</p>
  </section>
</body>
</html>
```